Sandwich Board and Poster design promoting a medical aesthetic clinic

I am looking for a clean, modern and relaxing design promoting a medical physician-led aesthetic clinic.
Services offered are neuromodulator treatment (Quelvo) and Dermal Fillers.
Logo must be included.
Use the tag line "Refresh your look, revive your spirit."
Address is 204-205 27361 92 Ave, Surrey, V7K 2M4
604-555-0148
email - info@lumawellpine.ca
www.lumawellpine.ca

```html
<!DOCTYPE html>
<html lang="en">
<head>
<meta charset="utf-8">
<title>Lumawell Pine – Clinic Poster</title>
<link rel="stylesheet" href="https://fonts.googleapis.com/css2?family=Prata&family=Montserrat:wght@400;500&display=swap">
<style>
  :root {
    --page: #eceef1;
    --navy: #1d3557;
    --gold: #d9a726;
    --gold-soft: #e7bd4a;
    --white: #ffffff;
    --photo-light: #f1ece8;
    --photo-mid: #d9c2b2;
    --skin-a: #e9cdb9;
    --skin-b: #c99a80;
  }
  * { margin: 0; padding: 0; box-sizing: border-box; }
  html, body { width: 986px; height: 1200px; overflow: hidden; background: var(--page); }
  .poster {
    position: absolute; left: 103px; top: 30px;
    width: 780px; height: 1140px;
    background: var(--navy); overflow: hidden;
  }
  .poster-art { position: absolute; inset: 0; }
  .headline {
    position: absolute; left: 60px; top: 710px;
    font-family: "Prata", serif; font-weight: 400;
    font-size: 66px; line-height: 1.04; color: var(--white);
    letter-spacing: -0.5px;
  }
  .brand {
    position: absolute; left: 540px; top: 770px; width: 200px;
    text-align: center;
  }
  .brand-mark {
    width: 66px; height: 66px; margin: 0 auto 12px;
    border: 2px solid var(--gold); border-radius: 50%;
  }
  .brand-name {
    font-family: "Montserrat", sans-serif; font-weight: 400;
    font-size: 16px; letter-spacing: 3px; color: var(--white);
    white-space: nowrap;
  }
  .services {
    position: absolute; left: 60px; top: 975px;
    font-family: "Prata", serif; color: var(--white);
  }
  .services-title { font-size: 24px; font-weight: 400; color: var(--gold); margin-bottom: 6px; }
  .services-list { list-style: none; font-size: 16px; line-height: 1.8; }
  .services-list li::before { content: "• "; }
  .contact {
    position: absolute; right: 34px; top: 955px;
    font-family: "Montserrat", sans-serif; font-style: normal; color: var(--white);
    text-align: right;
  }
  .contact-row { display: flex; justify-content: flex-end; align-items: center; gap: 7px; white-space: nowrap; }
  .contact-phone { font-family: "Prata", serif; font-size: 24px; margin-bottom: 8px; }
  .contact-small { font-size: 10px; margin-bottom: 8px; }
  .icon { width: 15px; height: 15px; flex: none; }
  .icon-lg { width: 18px; height: 18px; }
</style>
</head>
<body>
<main class="poster">
  <svg class="poster-art" width="780" height="1140" viewBox="0 0 780 1140">
    <defs>
      <linearGradient id="photoTone" x1="0" y1="0" x2="1" y2="0">
        <stop offset="0" stop-color="#d9c2b2"/>
        <stop offset="0.5" stop-color="#f1ece8"/>
        <stop offset="1" stop-color="#d9c2b2"/>
      </linearGradient>
      <radialGradient id="skinTone" cx="0.5" cy="0.45" r="0.6">
        <stop offset="0" stop-color="#e9cdb9"/>
        <stop offset="1" stop-color="#c99a80"/>
      </radialGradient>
    </defs>
    <rect class="hero-photo" x="0" y="0" width="780" height="400" fill="url(#photoTone)" role="img" aria-label="Photo of four women in profile facing each other"/>
    <path class="gold-wave" d="M0,330 Q390,270 780,345 L780,420 L0,420 Z" fill="#d9a726"/>
    <path class="navy-wave" d="M0,368 Q390,310 780,382 L780,1140 L0,1140 Z" fill="#1d3557"/>
    <g class="treatment-photos" stroke="#e7bd4a" stroke-width="6">
      <circle cx="112" cy="462" r="63" fill="url(#skinTone)" role="img" aria-label="Photo of a forehead injection treatment"/>
      <circle cx="266" cy="538" r="87" fill="url(#skinTone)" role="img" aria-label="Photo of a lip filler treatment"/>
      <circle cx="474" cy="470" r="141" fill="url(#skinTone)" role="img" aria-label="Photo of a woman receiving a brow injection"/>
      <circle cx="641" cy="594" r="63" fill="url(#skinTone)" role="img" aria-label="Photo of a cheek filler treatment"/>
    </g>
  </svg>

  <h1 class="headline">Refresh your<br>look, revive<br>your Spirit.</h1>

  <div class="brand">
    <div class="brand-mark"></div>
    <div class="brand-name">LUMAWELL PINE</div>
  </div>

  <section class="services">
    <h2 class="services-title">Our Services</h2>
    <ul class="services-list">
      <li>Neuromodulator treatment (Quelvo)</li>
      <li>Dermal Fillers</li>
    </ul>
  </section>

  <address class="contact">
    <div class="contact-row contact-phone">604-555-0148
      <svg class="icon icon-lg" viewBox="0 0 20 20"><circle cx="10" cy="10" r="9" fill="none" stroke="#d9a726" stroke-width="1.5"/><path d="M7 5.5l1.6 2.2-1 1.2a6 6 0 0 0 3.5 3.5l1.2-1 2.2 1.6-.8 1.6c-3.8.2-8-4-7.8-7.8z" fill="#d9a726"/></svg>
    </div>
    <div class="contact-row contact-small">204-205 27361 92 Ave, Surrey, V7K 2M4
      <svg class="icon" viewBox="0 0 16 16"><circle cx="8" cy="8" r="7.2" fill="none" stroke="#d9a726" stroke-width="1.2"/><path d="M8 3.5a3 3 0 0 0-3 3c0 2.2 3 5.8 3 5.8s3-3.6 3-5.8a3 3 0 0 0-3-3zm0 4.2a1.2 1.2 0 1 1 0-2.4 1.2 1.2 0 0 1 0 2.4z" fill="#d9a726"/></svg>
    </div>
    <div class="contact-row contact-small">info@lumawellpine.ca
      <svg class="icon" viewBox="0 0 16 16"><circle cx="8" cy="8" r="7.2" fill="none" stroke="#d9a726" stroke-width="1.2"/><rect x="4" y="5.2" width="8" height="5.6" fill="none" stroke="#d9a726" stroke-width="1"/><path d="M4 5.4l4 3 4-3" fill="none" stroke="#d9a726" stroke-width="1"/></svg>
      www.lumawellpine.ca
      <svg class="icon" viewBox="0 0 16 16"><circle cx="8" cy="8" r="7.2" fill="none" stroke="#d9a726" stroke-width="1.2"/><circle cx="8" cy="8" r="3.8" fill="none" stroke="#d9a726" stroke-width="1"/><path d="M4.2 8h7.6M8 4.2v7.6" stroke="#d9a726" stroke-width="0.8"/></svg>
    </div>
  </address>
</main>
</body>
</html>
```